DL flyer for mobile auto electrician

We need a DL flyer designed for distribution outlining the services provided by our mobile auto electrical business. Logo and text will be provided. The flyer will be distributed with the local newspaper and other advertising materials so we need something that will stand out from the crowd!

Our business is 'Brightpath Road Electrics' and our colours are blue and red which you will be able to see through the logo.

Industry/Entity Type

Electrician

```html
<!DOCTYPE html>
<html lang="en">
<head>
<meta charset="utf-8">
<title>Brightpath Road Electrics – DL Flyer</title>
<link rel="stylesheet" href="https://fonts.googleapis.com/css2?family=Montserrat:wght@700&family=Open+Sans:wght@600;700&display=swap">
<style>
  :root {
    --stage: #2b2b2b;
    --paper: #ffffff;
    --paper-shade: #eceef0;
    --red: #e3222f;
    --blue: #1590d2;
    --blue-deep: #1283c4;
    --pill-grey: #efefef;
    --white: #ffffff;
    --photo-a: #c9cfd4;
    --photo-b: #6d7a86;
  }
  * { box-sizing: border-box; margin: 0; padding: 0; }
  html, body { width: 806px; height: 1200px; overflow: hidden; }
  body { background: var(--stage); position: relative; font-family: "Open Sans", Arial, sans-serif; }

  .flyer {
    position: absolute; left: 143px; top: 85px;
    width: 520px; height: 1030px; overflow: hidden;
    background: linear-gradient(180deg, var(--paper) 40%, var(--paper-shade) 80%);
  }
  .flyer__art { position: absolute; inset: 0; }

  .brand-badge {
    position: absolute; left: 52px; top: 247px; width: 176px; height: 176px;
    border-radius: 50%; background: var(--white);
    border: 7px solid var(--red);
    display: flex; align-items: center; justify-content: center;
  }
  .brand-badge__inner {
    width: 146px; height: 146px; border-radius: 50%;
    border: 5px solid var(--blue);
    display: flex; align-items: center; justify-content: center; text-align: center;
  }
  .brand-badge__name {
    font-family: "Open Sans", Arial, sans-serif; font-weight: 700;
    font-size: 15px; line-height: 1.2; color: var(--blue);
  }

  .headline {
    position: absolute; left: 20px; right: 20px; top: 458px;
    font-family: "Montserrat", Arial, sans-serif; font-weight: 700;
    font-size: 18.5px; line-height: 25px; color: var(--red); text-align: center;
  }

  .service { position: absolute; display: flex; align-items: center;
    color: var(--white); font-weight: 600; font-size: 18px; }
  .service--blue { background: var(--blue); border-radius: 0 24px 24px 0; height: 56px; }
  .service--red { background: var(--red); border-radius: 24px; height: 46px; justify-content: center; }
  .service--grey { background: var(--pill-grey); border-radius: 28px; height: 56px; color: var(--red); }

  .service__icon {
    position: absolute; width: 68px; height: 68px; border-radius: 50%;
    display: flex; align-items: center; justify-content: center;
  }
  .service__icon--on-blue { background: var(--white); border: 3px solid var(--blue); }
  .service__icon--on-red { background: var(--red); border: 3px solid var(--white); box-shadow: 0 0 0 2px var(--red); }
  .service__icon svg { width: 38px; height: 38px; }

  .contact {
    position: absolute; left: 0; right: 0; top: 922px;
    color: var(--white); font-weight: 600; font-size: 19px; text-align: center; line-height: 28px;
  }
  .contact__line { display: flex; justify-content: center; align-items: center; gap: 8px; }
  .contact__line svg { width: 18px; height: 18px; }
</style>
</head>
<body>
<main class="flyer">
  <svg class="flyer__art" width="520" height="1030" viewBox="0 0 520 1030" aria-hidden="false">
    <defs>
      <clipPath id="photo-shape">
        <path d="M40 0 H520 V430 C420 420 320 400 250 360 C150 300 70 260 50 180 C40 120 38 60 40 0 Z"/>
      </clipPath>
    </defs>
    <path d="M0 0 H520 V446 C400 436 300 416 230 372 C130 310 30 270 0 190 Z" fill="var(--red)"/>
    <path d="M0 0 H24 C18 80 22 150 50 210 C80 270 150 320 230 372 C150 340 50 300 0 250 Z" fill="var(--paper)" opacity=".0"/>
    <rect x="0" y="0" width="520" height="440" fill="url(#photoFill)" clip-path="url(#photo-shape)" role="img" aria-label="Photo: auto electrician in a yellow hard hat working on wiring"/>
    <linearGradient id="photoFill" x1="0" y1="0" x2="1" y2="1">
      <stop offset="0" stop-color="var(--photo-a)"/>
      <stop offset="1" stop-color="var(--photo-b)"/>
    </linearGradient>
    <path d="M0 835 C150 800 330 770 520 750 V1030 H0 Z" fill="var(--blue-deep)"/>
  </svg>

  <div class="brand-badge">
    <div class="brand-badge__inner">
      <span class="brand-badge__name">Brightpath Road<br>Electrics</span>
    </div>
  </div>

  <h1 class="headline">Experienced mobile auto electrician servicing all residential, commercial and heavy duty vehicles</h1>

  <div class="service service--blue" style="left:55px; top:559px; width:418px; padding-left:88px;">Spotlights and dual battery systems</div>
  <div class="service__icon service__icon--on-blue" style="left:59px; top:553px;">
    <svg viewBox="0 0 40 40" fill="none" stroke="var(--blue)" stroke-width="2" stroke-linecap="round"><path d="M14 22a8 8 0 1 1 12 0c-2 2-2 4-2 6h-8c0-2 0-4-2-6z"/><path d="M16 31h8M17 34h6M20 4V1M8 9 6 7M32 9l2-2M4 18H1M36 18h3"/></svg>
  </div>

  <div class="service service--red" style="left:68px; top:624px; width:407px; padding-right:120px;">Air conditioning</div>
  <div class="service__icon service__icon--on-red" style="left:321px; top:613px;">
    <svg viewBox="0 0 40 40" fill="none" stroke="var(--white)" stroke-width="2"><rect x="4" y="10" width="32" height="20" rx="3"/><circle cx="15" cy="20" r="6"/><path d="M15 14v12M9 20h12M24 15h8M24 20h8M24 25h8"/></svg>
  </div>

  <div class="service service--blue" style="left:55px; top:677px; width:418px; padding-left:93px;">Camper trailers</div>
  <div class="service__icon service__icon--on-blue" style="left:59px; top:671px;">
    <svg viewBox="0 0 40 40" fill="none" stroke="var(--blue)" stroke-width="2"><path d="M3 28V12h26l6 8v8z"/><rect x="7" y="15" width="6" height="5"/><rect x="17" y="15" width="6" height="5"/><circle cx="11" cy="29" r="3" fill="var(--white)"/><circle cx="28" cy="29" r="3" fill="var(--white)"/></svg>
  </div>

  <div class="service service--red" style="left:68px; top:737px; width:407px; padding-right:120px;">Boats</div>
  <div class="service__icon service__icon--on-red" style="left:318px; top:723px;">
    <svg viewBox="0 0 40 40" fill="var(--white)"><path d="M19 4 9 24h10zM21 8v16h9z"/><path d="M6 27h28l-4 5H10z"/><path d="M4 35q4-2 8 0t8 0 8 0 8 0" fill="none" stroke="var(--white)" stroke-width="2"/></svg>
  </div>

  <div class="service service--blue" style="left:55px; top:790px; width:418px; padding-left:88px;">Mine site fit outs</div>
  <div class="service__icon service__icon--on-blue" style="left:64px; top:780px;">
    <svg viewBox="0 0 40 40" fill="none" stroke="var(--blue)" stroke-width="2"><path d="M4 6h32M20 6v6"/><rect x="12" y="12" width="16" height="12"/><path d="M8 36V24M32 36V24M4 36h32"/></svg>
  </div>

  <div class="service service--grey" style="left:68px; top:855px; width:410px; padding-left:24px;">All aspects of diagnosis and repairs</div>
  <div class="service__icon service__icon--on-red" style="left:419px; top:849px;">
    <svg viewBox="0 0 40 40" fill="none" stroke="var(--white)" stroke-width="3" stroke-linecap="round"><path d="M8 32 24 16M26 8a6 6 0 1 0 6 6l-4 0-2-2z"/><path d="M32 32 14 14M10 6l6 6-4 4-6-6z"/></svg>
  </div>

  <div class="contact">
    <div class="contact__line">Liam Calder
      <svg viewBox="0 0 20 20"><rect x="1" y="1" width="18" height="18" rx="4" fill="var(--white)"/><path d="M7 5c-1 0-2 1-2 2 0 5 4 8 8 8 1 0 2-1 2-2l-2-2-2 1c-1-1-2-2-3-3l1-2z" fill="var(--blue-deep)"/></svg>
      0412 558 907</div>
    <div class="contact__line">
      <svg viewBox="0 0 20 20"><rect x="1" y="4" width="18" height="12" fill="var(--white)"/><path d="M1 4l9 7 9-7" fill="none" stroke="var(--blue-deep)" stroke-width="1.5"/></svg>
      lcalder@brightpath.com.au</div>
    <div class="contact__line">ABN 51 824 300 617 AU48203</div>
  </div>
</main>
</body>
</html>
```